Business Card Design for an Investment Company

We need a business card design for our private investment company, called Dunmore Equity. Dunmore Equity is an investments partnership that aims to acquire shares in listed companies with a view to influencing those companies through active dialogue in order to improve their value. We need designs that use the logo colors (blue, grey, white), we need both English and Arabic on the business cards (can be on one side or 2 sides). The final logo should communicate professionalism, conservatism (nothing too fancy or too cheesy), that we are smart, conservative and old school.

Target Market(s)

Investment companies

Industry/Entity Type

Investment

Contact Information for Business Card

Tariq Salmanuddin Farouqi
Senior Executive Officer

Harbor Court 07, Level 3, Office 214/12
QTFZ

+9714987650
tfarouqi@dunmore-equity.com
www.dunmore-equity.com

Requirements
Must have
• Logo to be placed on the left hand side of the business card
• for the Arabic, we only need to have the name and title so it can be accomodated on one side so we can have the other side with full color and logo. The arabic that needs to be used is the below:
• طارق سلمان الدين فاروقي
• المدير التنفيدي

```html
<!DOCTYPE html>
<html lang="en">
<head>
<meta charset="utf-8">
<title>Dunmore Equity – Business Card</title>
<link rel="stylesheet" href="https://fonts.googleapis.com/css2?family=Open+Sans:wght@400;600;700&family=Noto+Kufi+Arabic:wght@400;700&display=swap">
<style>
  :root {
    --stage: #3b3532;
    --card: #151617;
    --card-edge: #0c0c0d;
    --brand-blue: #2c7bb6;
    --brand-grey: #5d5f62;
    --ink: #f1f1f1;
    --muted: #a9abae;
  }
  * { box-sizing: border-box; margin: 0; padding: 0; }
  html, body {
    width: 1200px; height: 864px; overflow: hidden;
    background: var(--stage);
    font-family: "Open Sans", Arial, sans-serif;
  }
  .stage { position: relative; width: 1200px; height: 864px; }
  .card {
    position: absolute; width: 540px; height: 309px;
    background: var(--card);
    border: 1px solid var(--card-edge);
    box-shadow: 0 14px 30px rgba(0,0,0,.45);
  }
  .card--back { left: 70px; top: 110px; }
  .card--front { left: 590px; top: 430px; }

  .wordmark {
    position: absolute; left: 36px; display: flex; align-items: center; gap: 12px;
    font-weight: 700; color: var(--brand-blue); letter-spacing: -0.5px;
    font-size: 42px; line-height: 1; white-space: nowrap;
  }
  .wordmark__square { width: 24px; height: 24px; background: var(--brand-grey); }
  .card--back .wordmark { top: 84px; }
  .card--front .wordmark { top: 48px; }

  .web {
    position: absolute; left: 72px; top: 150px;
    font-size: 13px; letter-spacing: 5px; color: var(--muted);
  }

  .arabic {
    position: absolute; right: 36px; bottom: 34px;
    direction: rtl; text-align: right;
    font-family: "Noto Kufi Arabic", "Open Sans", sans-serif;
    color: var(--ink);
  }
  .arabic__name { color: var(--brand-blue); font-weight: 700; font-size: 17px; line-height: 1.6; }
  .arabic__title { font-size: 13px; line-height: 1.6; }

  .details {
    position: absolute; left: 36px; top: 150px; width: 470px;
    display: flex; align-items: stretch;
  }
  .person {
    flex: none; padding-right: 18px;
    color: var(--ink); font-size: 12.5px; line-height: 1.55;
  }
  .person__name { color: var(--brand-blue); font-weight: 700; font-size: 13px; letter-spacing: .3px; }
  .divider { flex: none; width: 1px; background: var(--ink); opacity: .8; }
  .contact { list-style: none; padding-left: 18px; color: var(--ink); font-size: 12.5px; line-height: 1.6; }
  .contact li { display: flex; align-items: center; gap: 8px; white-space: nowrap; }
  .contact svg { width: 11px; height: 11px; fill: var(--brand-blue); flex: none; }
</style>
</head>
<body>
<main class="stage">
  <section class="card card--back" aria-label="Card back">
    <div class="wordmark"><span class="wordmark__square"></span>Dunmore Equity</div>
    <p class="web">www.dunmore-equity.com</p>
    <div class="arabic" lang="ar">
      <p class="arabic__name">طارق سلمان الدين فاروقي</p>
      <p class="arabic__title">المدير التنفيدي</p>
    </div>
  </section>

  <section class="card card--front" aria-label="Card front">
    <div class="wordmark"><span class="wordmark__square"></span>Dunmore Equity</div>
    <div class="details">
      <div class="person">
        <p class="person__name">TARIQ SALMANUDDIN FAROUQI</p>
        <p>SENIOR EXECUTIVE OFFICER</p>
        <p>Harbor Court 07, Level 3,</p>
        <p>Office 214/12</p>
        <p>QTFZ</p>
      </div>
      <span class="divider"></span>
      <ul class="contact">
        <li><svg viewBox="0 0 12 12" aria-hidden="true"><path d="M2.5 0.5l2 2.5-1.2 1.4c.7 1.5 2 2.8 3.5 3.5l1.4-1.2 2.5 2-1.3 2.3C4.7 10.8 1.2 7.3.2 2z"/></svg>+9714987650</li>
        <li><svg viewBox="0 0 12 12" aria-hidden="true"><path d="M3 0h6v12H3zM4 1.5v8h4v-8z"/></svg>+9714987651</li>
        <li><svg viewBox="0 0 12 12" aria-hidden="true"><path d="M3 0h6v3H3zM0 4h12v6H9v2H3v-2H0zM4 8v3h4V8z"/></svg>+9714987652</li>
        <li><svg viewBox="0 0 12 12" aria-hidden="true"><path d="M0 2h12v1L6 7 0 3zM0 4.5l6 4 6-4V10H0z"/></svg>tfarouqi@dunmore-equity.com</li>
      </ul>
    </div>
  </section>
</main>
</body>
</html>
```